Crestline Lending Group Business Cards

We are looking to revamp the current business cards each of our locations uses. We are a lending company that specializes in personal loans, title loans, and tax services. We have locations in New Mexico, Texas, and Oklahoma.

We would like a cleaner, sleeker look while still highlighting what we offer. Title Loans, Personal Loans & Tax Services. We also want to include our referral fee somewhere on the card. We would like to see an English option as well as a Spanish option for the cards.

PLEASE NOTE: Some business cards do not include the employee's name but just the store's location, while others will include both.

These are double-sided business cards, and we would like to see proof if possible. I have included proofs of our current business cards for you to review below, as well as our company logo. Feel free to get creative with the logo, etc! Colors should match the logo; however, you do not need to use all of our logo colors if you don't want to.

```html
<!DOCTYPE html>
<html lang="en">
<head>
<meta charset="utf-8">
<title>Crestline Lending Group – Business Card</title>
<link rel="stylesheet" href="https://fonts.googleapis.com/css2?family=Oswald:wght@400;500;600&family=Montserrat:wght@700;800;900&family=Open+Sans:wght@400;600&display=swap">
<style>
  :root {
    --bg: #7f97b8;
    --card-white: #ffffff;
    --brand-green: #1d6137;
    --brand-red: #d3242c;
    --brand-red-deep: #c71f27;
    --text-white: #ffffff;
  }
  * { box-sizing: border-box; margin: 0; padding: 0; }
  html, body {
    width: 1200px; height: 876px; overflow: hidden;
    background: var(--bg);
  }
  .sheet {
    width: 1200px; height: 876px;
    display: flex; align-items: center; justify-content: center; gap: 48px;
  }
  .card {
    position: relative;
    width: 520px; height: 300px;
    border-radius: 26px;
    overflow: hidden;
    box-shadow: 0 10px 24px rgba(30, 45, 70, .28);
  }

  /* Front */
  .card-front { background: var(--card-white); }
  .identity {
    position: absolute; top: 34px; left: 0; right: 0;
    text-align: center;
  }
  .person-name {
    font-family: "Montserrat", sans-serif; font-weight: 800;
    font-size: 19px; letter-spacing: .5px; color: var(--brand-red);
  }
  .person-name .surname { color: var(--brand-green); }
  .person-title {
    font-family: "Open Sans", sans-serif; font-size: 12px;
    color: var(--brand-green); margin-top: 2px;
  }
  .company {
    margin-top: 16px;
    display: flex; align-items: center; justify-content: center; gap: 10px;
  }
  .company-dot {
    width: 14px; height: 14px; border-radius: 50%;
    background: var(--brand-red);
  }
  .company-name {
    font-family: "Open Sans", sans-serif; font-weight: 600;
    font-size: 25px; color: var(--brand-green);
  }
  .company-web {
    font-family: "Open Sans", sans-serif; font-size: 11.5px;
    color: var(--brand-red); margin-top: 4px;
  }
  .services-band {
    position: absolute; left: 0; right: 0; top: 168px; height: 34px;
    background: var(--brand-green);
    display: flex; align-items: center; justify-content: center; gap: 30px;
    font-family: "Oswald", sans-serif; font-weight: 500;
    font-size: 15px; letter-spacing: .3px; color: var(--text-white);
    text-transform: uppercase;
  }
  .services-band .sep {
    width: 9px; height: 9px; border-radius: 50%; background: var(--text-white);
  }
  .contacts {
    position: absolute; left: 22px; right: 22px; top: 222px; height: 58px;
    display: flex; align-items: center; justify-content: space-between;
    font-family: "Oswald", sans-serif; font-size: 13px;
    color: var(--brand-green); line-height: 1.25;
  }
  .contact { display: flex; align-items: center; gap: 8px; }
  .contact-icon {
    width: 22px; height: 22px; flex: none;
    border-radius: 50%; background: var(--brand-red);
    display: flex; align-items: center; justify-content: center;
  }
  .contact-rule { width: 1.5px; height: 30px; background: var(--brand-red); }

  /* Back */
  .card-back { background: var(--brand-red-deep); }
  .dollar-texture {
    position: absolute; inset: 0;
    background: linear-gradient(135deg, #d9313a 0%, var(--brand-red-deep) 55%, #c21d25 100%);
  }
  .referral-band {
    position: absolute; left: 0; right: 0; top: 36px; height: 44px;
    background: var(--brand-green);
    display: flex; align-items: center; justify-content: center;
    font-family: "Montserrat", sans-serif; font-weight: 800;
    font-size: 24px; letter-spacing: .5px; color: var(--text-white);
    text-transform: uppercase;
  }
  .offer {
    position: absolute; left: 0; right: 0; top: 104px;
    text-align: center; color: var(--text-white);
    font-family: "Montserrat", sans-serif; font-weight: 900;
  }
  .offer-lead {
    display: inline-flex; align-items: center; gap: 6px;
    font-size: 46px; line-height: 1;
  }
  .offer-lead .upto {
    font-size: 15px; font-weight: 700; line-height: 1; text-align: left;
  }
  .offer-amount { font-size: 104px; line-height: 1; letter-spacing: -2px; }
</style>
</head>
<body>
<main class="sheet">

  <section class="card card-front" aria-label="Business card front">
    <div class="identity">
      <p class="person-name">DANA <span class="surname">REYES</span></p>
      <p class="person-title">Branch Manager</p>
      <div class="company">
        <span class="company-dot"></span>
        <span class="company-name">Crestline Lending Group</span>
      </div>
      <p class="company-web">www.crestlinelending.com</p>
    </div>

    <div class="services-band">
      <span>Title Loans</span><span class="sep"></span>
      <span>Personal Loans</span><span class="sep"></span>
      <span>Tax Services</span>
    </div>

    <div class="contacts">
      <div class="contact">
        <span class="contact-icon">
          <svg width="12" height="12" viewBox="0 0 24 24" aria-hidden="true"><path fill="#fff" d="M6.6 10.8a15 15 0 0 0 6.6 6.6l2.2-2.2a1 1 0 0 1 1-.25 11.4 11.4 0 0 0 3.6.57 1 1 0 0 1 1 1V20a1 1 0 0 1-1 1A17 17 0 0 1 3 4a1 1 0 0 1 1-1h3.5a1 1 0 0 1 1 1c0 1.25.2 2.45.57 3.57a1 1 0 0 1-.25 1z"/></svg>
        </span>
        <span>(505) 555-0148</span>
      </div>
      <span class="contact-rule"></span>
      <div class="contact">
        <span class="contact-icon">
          <svg width="12" height="12" viewBox="0 0 24 24" aria-hidden="true"><path fill="#fff" d="M12 2a7 7 0 0 0-7 7c0 5.2 7 13 7 13s7-7.8 7-13a7 7 0 0 0-7-7zm0 9.5A2.5 2.5 0 1 1 12 6.5a2.5 2.5 0 0 1 0 5z"/></svg>
        </span>
        <span>48 Mesa Ridge Road, Suite B,<br>Clearwater, TX 79001</span>
      </div>
      <span class="contact-rule"></span>
      <div class="contact">
        <span class="contact-icon">
          <svg width="12" height="12" viewBox="0 0 24 24" aria-hidden="true"><path fill="#fff" d="M3 5h18v14H3zm2 2v.4l7 5 7-5V7zm0 2.9V17h14V9.9l-7 5z"/></svg>
        </span>
        <span>dreyes@crestlinelending.com</span>
      </div>
    </div>
  </section>

  <section class="card card-back" aria-label="Business card back">
    <div class="dollar-texture" role="img" aria-label="Repeating pattern of faint dollar signs on red"></div>
    <div class="referral-band">Refer a Friend</div>
    <div class="offer">
      <div class="offer-lead">GET <span class="upto">UP<br>TO</span></div>
      <div class="offer-amount">$100</div>
    </div>
  </section>

</main>
</body>
</html>
```